GracefulDme Business Cards

I am looking for some business cards for my business. I would like them to elegant, classy, etc.

Information Includes

Please see the the content below:

Lorinda K. Pratt

Brand titles:

Empowerment Specialist
Speaker/Workshop Facilitator

Taking you from where you are to where you're purposed to be!

Contact Information
Email - GracefulDmeOutreach@[url removed, login to view]
Facebook - [url removed, login to view]
Instagram - GracefulDme

I have attached the photos.

I am interested in possibly Orange, White, Gray concept. But open to other ideas

```html
<!DOCTYPE html>
<html lang="en">
<head>
<meta charset="utf-8">
<title>GracefulDme Business Cards</title>
<link rel="stylesheet" href="https://fonts.googleapis.com/css2?family=Roboto:wght@400;500&family=Lobster&display=swap">
<style>
  :root {
    --bg: #2b2b2b;
    --card: #ffffff;
    --orange: #f07c1e;
    --gray: #555555;
    --photo-top: #e6e2df;
    --photo-mid: #8a8585;
    --photo-bottom: #e0413f;
  }
  * { margin: 0; padding: 0; box-sizing: border-box; }
  html, body { width: 1200px; height: 900px; overflow: hidden; }
  body {
    background: var(--bg);
    font-family: "Roboto", Arial, sans-serif;
    position: relative;
  }
  .card {
    position: absolute;
    left: 280px;
    width: 640px;
    height: 366px;
    background: var(--card);
    border-radius: 26px;
    overflow: hidden;
  }
  .card--info { top: 68px; }
  .card--portrait { top: 466px; }

  .identity {
    position: absolute;
    left: 56px;
    top: 148px;
  }
  .identity__name {
    color: var(--orange);
    font-size: 30px;
    font-weight: 400;
    line-height: 1.1;
    margin-bottom: 6px;
  }
  .identity__title {
    color: var(--gray);
    font-size: 14px;
    line-height: 1.35;
  }
  .divider {
    position: absolute;
    left: 338px;
    top: 126px;
    width: 2px;
    height: 96px;
    background: var(--orange);
  }
  .contacts {
    position: absolute;
    left: 366px;
    top: 136px;
    list-style: none;
  }
  .contacts__item {
    display: flex;
    align-items: center;
    gap: 9px;
    color: var(--gray);
    font-size: 14px;
    line-height: 1;
    margin-bottom: 12px;
  }
  .contacts__mark {
    width: 12px;
    height: 12px;
    border-radius: 50%;
    background: var(--orange);
    flex: none;
  }

  .portrait {
    position: absolute;
    left: 48px;
    top: 40px;
    width: 236px;
    height: 326px;
    border-radius: 110px 110px 0 0;
    background: linear-gradient(180deg, var(--photo-top) 0%, var(--photo-mid) 45%, var(--photo-mid) 62%, var(--photo-bottom) 78%, var(--photo-bottom) 100%);
  }
  .signature-name {
    position: absolute;
    left: 300px;
    top: 120px;
    color: var(--orange);
    font-family: "Lobster", cursive;
    font-size: 46px;
    font-weight: 400;
    white-space: nowrap;
  }
</style>
</head>
<body>
  <section class="card card--info">
    <div class="identity">
      <h1 class="identity__name">Lorinda K. Pratt</h1>
      <p class="identity__title">Evangelist</p>
      <p class="identity__title">Empowerment Specialist</p>
      <p class="identity__title">Speaker/Workshop Facilitator</p>
    </div>
    <div class="divider"></div>
    <ul class="contacts">
      <li class="contacts__item"><span class="contacts__mark"></span>GracefulDmeOutreach@postnest.net</li>
      <li class="contacts__item"><span class="contacts__mark"></span>Socialhub.com/GracefulDme</li>
      <li class="contacts__item"><span class="contacts__mark"></span>GracefulDme</li>
    </ul>
  </section>

  <section class="card card--portrait">
    <div class="portrait" role="img" aria-label="Photo of Lorinda K. Pratt standing with arms crossed, in a striped blouse and red skirt"></div>
    <h2 class="signature-name">Lorinda K. Pratt</h2>
  </section>
</body>
</html>
```